New London Job Board - Business Card Required

Dear All,

I own Quintaro Limited, which in turn owns the website:
www.brambletopfield.com

I want all of you wonderful creative people to come up with a slick, and awesome business card design that incorporates the logo on the site, and some colouring and design elements from it.

You have free reign in how you go about doing this, I won't be giving my contact details on this platform, but the winner will be asked to redesign based on my contact details which I will supply at the end.

I need the design to be completed within 5 days. I need the final print copies of the business cards by the 25th November, so unfortunately it's a bit of a rush to get these designs ready.

Any questions, please ask.

Thank you

Thank you all for your hard work and exceptional designs provided. I do have to pick one, so I have a very clear idea of which one this is, however I will wait one further day until the competition closes to be fair to all those have submitted, or are in the process of submitting. I wish you all the best and thank you again for your dedication.

```html
<!DOCTYPE html>
<html lang="en">
<head>
<meta charset="utf-8">
<title>Bramble Topfield – Business Card</title>
<link rel="stylesheet" href="https://fonts.googleapis.com/css2?family=Marcellus&display=swap">
<style>
  :root {
    --page: #ece7da;
    --card-black: #111111;
    --card-band: #050505;
    --gold: #d8b13c;
    --gold-deep: #c49a22;
    --gold-mid: #dcc44b;
    --gold-pale: #efe282;
    --gold-tab: #e3d46b;
    --ink: #2a1f08;
    --icon: #6b3a10;
  }
  * { box-sizing: border-box; margin: 0; padding: 0; }
  html, body {
    width: 1200px; height: 1000px; overflow: hidden;
    background: var(--page);
    font-family: "Marcellus", serif;
  }
  .card {
    position: absolute; left: 250px;
    width: 700px; height: 400px;
    background: var(--card-black);
    box-shadow: 0 10px 24px rgba(0,0,0,.28);
    overflow: hidden;
  }
  .card--front { top: 60px; }
  .card--back { top: 540px; }

  /* front */
  .brand {
    position: absolute; left: 70px; top: 150px;
    display: flex; align-items: center; gap: 14px;
    color: var(--gold);
    font-size: 30px; letter-spacing: 2px; text-transform: uppercase;
  }
  .brand__dot {
    width: 22px; height: 22px; border-radius: 50%;
    background: var(--gold);
  }
  .name-tab {
    position: absolute; right: 0; top: 120px;
    width: 290px; height: 72px;
    background: var(--gold-tab);
    clip-path: polygon(10% 0, 100% 0, 100% 100%, 0 100%, 4% 40%);
    border-top-left-radius: 12px;
    text-align: right; padding: 14px 22px 0 0;
    color: var(--ink);
  }
  .name-tab__name { font-size: 24px; letter-spacing: .5px; }
  .name-tab__role { font-size: 12px; letter-spacing: 1px; margin-top: 2px; }
  .band {
    position: absolute; left: 0; top: 250px; width: 100%; height: 42px;
    background: var(--card-band);
  }
  .contacts {
    position: absolute; left: 0; top: 292px; width: 100%; height: 108px;
    display: grid; grid-template-columns: 230px 214px 1fr; gap: 4px;
    background: var(--card-band);
  }
  .contacts__cell {
    display: flex; flex-direction: column; justify-content: center;
    gap: 8px; padding-left: 36px;
    font-size: 13px; color: var(--ink);
  }
  .contacts__cell--address { background: var(--gold-pale); padding-left: 50px; }
  .contacts__cell--phone { background: var(--gold-mid); }
  .contacts__cell--web { background: var(--gold-deep); }
  .line { display: flex; align-items: center; gap: 10px; }
  .line svg { width: 16px; height: 14px; fill: var(--icon); flex: none; }

  /* back */
  .frame {
    position: absolute; inset: 34px 40px;
    border: 2px solid var(--gold-pale);
  }
  .brand--center {
    left: 50%; top: 50%; transform: translate(-50%, -50%);
    font-size: 38px;
  }
</style>
</head>
<body>

<section class="card card--front" aria-label="Business card front">
  <div class="brand"><span class="brand__dot"></span>Bramble Topfield</div>

  <div class="name-tab">
    <div class="name-tab__name">YOUR NAME</div>
    <div class="name-tab__role">DESIGNATION</div>
  </div>

  <div class="band"></div>

  <div class="contacts">
    <div class="contacts__cell contacts__cell--address">
      <div class="line">
        <svg viewBox="0 0 16 14"><path d="M8 0 0 7h2v7h4V9h4v5h4V7h2z"/></svg>
        <span>123 ABC Avenue</span>
      </div>
      <div class="line"><span style="padding-left:26px">ABCD 54321</span></div>
    </div>
    <div class="contacts__cell contacts__cell--phone">
      <div class="line">
        <svg viewBox="0 0 16 14"><path d="M1 4c0-2 3-3 7-3s7 1 7 3v1h-4V3.5H5V5H1zM3 6h10l2 7H1z"/></svg>
        <span>000 . 1234 . 5678</span>
      </div>
      <div class="line">
        <svg viewBox="0 0 16 14"><path d="M4 0h8v4H4zM1 5h14v6h-3V8H4v3H1zM5 9h6v5H5z"/></svg>
        <span>000 . 9876 . 5432</span>
      </div>
    </div>
    <div class="contacts__cell contacts__cell--web">
      <div class="line">
        <svg viewBox="0 0 16 14"><path d="M0 1h16v12H0zM1.5 2.5 8 8l6.5-5.5z" fill-rule="evenodd"/></svg>
        <span>name@email.com</span>
      </div>
      <div class="line">
        <svg viewBox="0 0 16 14"><path d="M0 0h16v10H0zM1.5 1.5v7h13v-7zM6 11h4v1.5h2V14H4v-1.5h2z" fill-rule="evenodd"/></svg>
        <span>www.website.com</span>
      </div>
    </div>
  </div>
</section>

<section class="card card--back" aria-label="Business card back">
  <div class="frame"></div>
  <div class="brand brand--center"><span class="brand__dot"></span>Bramble Topfield</div>
</section>

</body>
</html>
```